Erstellung einer ersten Einladungskarte „Safe the Date“
Zielgruppe
Spezialist für temporäres Linienmanagement & Projektmanagement
Als Sozietät für professionelles Interim Management bündelt die brückwerk AG die fachliche Kompetenz und die langjährige Erfahrung erfolgreicher Führungspersönlichkeiten aus nahezu allen Sektoren der Wirtschaft. Wir unterstützen unsere Kunden bei der Bewältigung temporärer Herausforderungen im Linienmanagement sowie im Management komplexer strategischer Projekte und Programme.
https://www.brueckwerk-example.net/de/home.html
Aufgabenstellung
Siehe angehängtes Briefing und angehängtes CD Manual, das nicht zwingend eingehalten werden muss für diesen Job

```html
<!DOCTYPE html>
<html lang="de">
<head>
<meta charset="utf-8">
<title>Save the Date – Dezember</title>
<link rel="stylesheet" href="https://fonts.googleapis.com/css2?family=Titillium+Web:wght@400;600&display=swap">
<style>
  :root {
    --paper: #fbfbfb;
    --page: #ffffff;
    --ink-blue: #42677f;
    --ink-soft: #9eb0c0;
    --accent: #e8600f;
    --accent-soft: #f3a774;
    --grid: #6f8aa0;
  }
  html, body {
    margin: 0;
    width: 1200px;
    height: 1200px;
    overflow: hidden;
    background: var(--page);
    font-family: "Titillium Web", sans-serif;
  }
  .invitation-card {
    position: absolute;
    left: 54px;
    top: 334px;
    width: 1092px;
    height: 520px;
    background: var(--paper);
    overflow: hidden;
  }
  .calendar {
    position: absolute;
    inset: 0;
    width: 1092px;
    height: 520px;
  }
  .calendar .grid-line { stroke: var(--grid); stroke-width: 1.4; }
  .calendar .month-title { font-family: "Titillium Web", sans-serif; font-weight: 600; font-size: 32px; fill: var(--ink-blue); }
  .calendar .weekday { font-family: "Titillium Web", sans-serif; font-size: 17px; fill: var(--ink-blue); text-anchor: end; }
  .calendar .day-number { font-family: "Titillium Web", sans-serif; font-weight: 600; font-size: 34px; fill: var(--ink-blue); }
  .calendar .faded { opacity: 0.55; }
  .calendar .marker-ring { fill: none; stroke: var(--accent); stroke-width: 5; stroke-linecap: round; }
  .figure-area { position: absolute; border-radius: 3px; }
  .crowd-office {
    left: 266px; top: 194px; width: 330px; height: 64px;
    background: linear-gradient(90deg, var(--ink-soft), var(--ink-blue) 55%, var(--accent-soft));
  }
  .crowd-party {
    left: 620px; top: 172px; width: 262px; height: 86px;
    background: linear-gradient(90deg, var(--accent-soft), var(--accent) 55%, var(--ink-soft));
  }
  .single-person { width: 16px; height: 58px; background: var(--ink-blue); }
  .single-person.pale { background: var(--ink-soft); }
  .host-figure {
    left: 748px; top: 454px; width: 156px; height: 66px;
    background: var(--ink-blue);
  }
  .speech-box {
    position: absolute;
    left: 910px; top: 407px;
    width: 157px; height: 85px;
    background: var(--accent);
    color: #fff;
    font-size: 21px;
    display: flex; align-items: center; justify-content: center;
  }
  .speech-box::before {
    content: "";
    position: absolute;
    left: -17px; top: 48px;
    border-right: 17px solid var(--accent);
    border-bottom: 14px solid transparent;
  }
</style>
</head>
<body>
  <section class="invitation-card">
    <svg class="calendar" viewBox="0 0 1092 520" aria-label="Kalenderausschnitt Dezember">
      <text class="month-title" x="170" y="102">Dezember</text>

      <line class="grid-line" x1="0" y1="126" x2="1092" y2="126"/>
      <line class="grid-line" x1="0" y1="262" x2="1092" y2="262"/>
      <line class="grid-line" x1="0" y1="410" x2="1092" y2="410"/>
      <line class="grid-line" x1="166" y1="126" x2="166" y2="520"/>
      <line class="grid-line" x1="438" y1="126" x2="438" y2="520"/>
      <line class="grid-line" x1="708" y1="126" x2="708" y2="520"/>
      <line class="grid-line" x1="978" y1="126" x2="978" y2="410"/>

      <text class="weekday" x="154" y="150">Donnerstag</text>
      <text class="day-number" x="178" y="160">1</text>
      <text class="weekday" x="426" y="150">Freitag</text>
      <text class="day-number" x="452" y="160">2</text>
      <text class="weekday" x="696" y="150">Samstag</text>
      <text class="day-number" x="722" y="160">3</text>
      <text class="weekday" x="966" y="150">Sonntag</text>
      <text class="day-number" x="992" y="160">4</text>

      <text class="weekday" x="154" y="288">Donnerstag</text>
      <text class="day-number" x="178" y="298">8</text>
      <text class="weekday" x="426" y="288">Freitag</text>
      <text class="day-number" x="452" y="298">9</text>
      <text class="weekday" x="696" y="288">Samstag</text>
      <text class="day-number" x="722" y="298">10</text>
      <text class="weekday" x="966" y="288">Sonntag</text>
      <text class="day-number" x="992" y="298">11</text>

      <g class="faded">
        <text class="weekday" x="154" y="436">Donnerstag</text>
        <text class="day-number" x="178" y="446">15</text>
        <text class="weekday" x="426" y="436">Freitag</text>
        <text class="day-number" x="452" y="446">16</text>
        <text class="weekday" x="696" y="436">Samstag</text>
        <text class="day-number" x="722" y="446">17</text>
      </g>

      <ellipse class="marker-ring" cx="468" cy="164" rx="384" ry="108" transform="rotate(-6 468 164)"/>
    </svg>

    <div class="figure-area crowd-office" role="img" aria-label="Silhouetten von Geschäftsleuten im Gespräch"></div>
    <div class="figure-area crowd-party" role="img" aria-label="Silhouetten feiernder, springender Menschen"></div>
    <div class="figure-area single-person" style="left:142px;top:200px" role="img" aria-label="Silhouette einer einzelnen Person"></div>
    <div class="figure-area single-person" style="left:146px;top:348px" role="img" aria-label="Silhouette einer einzelnen Person"></div>
    <div class="figure-area single-person" style="left:418px;top:348px" role="img" aria-label="Silhouette einer einzelnen Person"></div>
    <div class="figure-area single-person" style="left:688px;top:348px" role="img" aria-label="Silhouette einer einzelnen Person"></div>
    <div class="figure-area single-person pale" style="left:952px;top:348px" role="img" aria-label="Silhouette einer einzelnen Person"></div>
    <div class="figure-area host-figure" role="img" aria-label="Silhouette eines Geschäftsmanns mit Knoten am Finger als Erinnerung"></div>

    <div class="speech-box">Safe the date!</div>
  </section>
</body>
</html>
```